Flyer Design Project

opening a preschool and need to hand out flyers to advertise at an expo on Feb.1st. It is geared toward 3-4 year old potty trained children. I have more that 10+ years teaching experience and it will be a private preschool with small class sizes and individual instruction and attention. You can look at the website, it is www.brambleoakacademy.net. I tried to make a flyer but I can't make it with high enough resolution. I attached the logo and my attempted flyer.

Industry/Entity Type

Preschool

```html
<!DOCTYPE html>
<html lang="en">
<head>
<meta charset="utf-8">
<title>Bramble Oak Academy – Now Enrolling</title>
<link href="https://fonts.googleapis.com/css2?family=Architects+Daughter&family=Arimo:wght@400;700&display=swap" rel="stylesheet">
<style>
:root{
  --mint:#d5ecec;
  --teal:#48b3b3;
  --teal-deep:#1f8f8f;
  --sky:#2bb5de;
  --ink:#2f2f2f;
  --white:#ffffff;
  --ribbon:#d9e6e6;
  --band:#cde8e8;
}
*{margin:0;padding:0;box-sizing:border-box}
html,body{width:779px;height:1200px;overflow:hidden;background:var(--mint)}
.flyer{position:relative;width:779px;height:1200px;overflow:hidden;background:var(--mint);font-family:"Arimo",Arial,sans-serif;color:var(--white)}
.backdrop{position:absolute;inset:0}
.brand{position:absolute;left:24px;top:136px;width:320px;text-align:center;color:var(--ink);white-space:nowrap}
.brand-mark{display:inline-block;width:12px;height:12px;border-radius:50%;background:var(--ink);vertical-align:middle;margin-right:7px}
.brand-name{font-weight:700;font-size:20px;letter-spacing:.3px;vertical-align:middle}
.brand-tagline{display:block;font-size:11px;margin-top:6px}
.address{position:absolute;left:24px;top:188px;width:320px;text-align:center;color:var(--ink);font-size:16px;line-height:21px}
.contact{position:absolute;left:368px;top:78px;color:var(--ink);list-style:none}
.contact li{display:flex;align-items:center;height:29px}
.contact svg{width:18px;height:18px;margin-right:14px;flex:none}
.contact .web{font-weight:700;font-size:20px}
.contact .mail{font-size:14px}
.contact .phone{font-size:23px}
.hands{position:absolute;left:473px;top:196px;width:214px;height:88px;border-radius:40px 40px 8px 8px;background:linear-gradient(90deg,#f0a35a,#f3d46a,#8fd07a,#e98aa8,#f7b96a)}
.ribbon{position:absolute;left:432px;top:280px;width:286px;height:62px;transform:rotate(-5deg)}
.ribbon-text{position:absolute;left:0;top:0;width:100%;line-height:62px;text-align:center;color:var(--ink);font-weight:700;font-size:21px}
.hand{font-family:"Architects Daughter",cursive;text-transform:uppercase}
.about-title{position:absolute;left:56px;top:352px;width:334px;text-align:center;color:var(--ink);font-size:24px;font-weight:400}
.about{position:absolute;left:56px;top:398px;width:342px;font-weight:700;font-size:17.3px;line-height:22.5px}
.about p{margin-bottom:12px}
.about u{text-decoration:underline}
.special{position:absolute;left:496px;top:356px;width:214px;text-align:center;font-size:18.5px;line-height:26px;letter-spacing:.5px}
.offer-title{position:absolute;left:478px;top:486px;width:262px;text-align:center;color:var(--ink);font-size:28px;font-weight:400}
.offer{position:absolute;left:482px;top:540px;width:246px;list-style:none;font-weight:700;font-size:17.3px;line-height:21.5px}
.offer li{position:relative;padding-left:33px;margin-bottom:10px}
.offer li svg{position:absolute;left:0;top:2px;width:18px;height:18px}
.offer em{font-style:italic}
.kids{position:absolute;left:116px;top:862px;width:552px;height:110px;border-radius:50px;background:linear-gradient(90deg,#f6d37a,#ea8fb0,#7cc4e6,#a6d47e,#f2a566)}
.enroll-band{position:absolute;left:0;top:975px;width:779px;height:130px;background:var(--band);text-align:center;color:var(--ink)}
.enroll-title{font-size:40px;color:var(--teal-deep);margin-top:14px;line-height:46px;text-transform:none;font-variant:small-caps;font-weight:400}
.enroll-call{font-size:22px;margin-top:2px;letter-spacing:.6px}
.enroll-forms{font-size:18px;margin-top:2px;letter-spacing:.6px}
.footnote{position:absolute;left:0;top:1125px;width:779px;text-align:center;color:#3d4a4a;font-weight:700;font-size:15px}
</style>
</head>
<body>
<main class="flyer">
  <svg class="backdrop" width="779" height="1200" viewBox="0 0 779 1200" aria-hidden="true">
    <rect width="779" height="1200" fill="var(--mint)"/>
    <path d="M0 228 C120 270 220 315 330 300 C470 282 560 195 779 148 L779 1200 L0 1200 Z" fill="var(--teal)"/>
    <path d="M0 222 C120 262 220 306 330 292 C470 274 560 187 779 140" fill="none" stroke="#bfe7ee" stroke-width="10"/>
    <path d="M0 228 C120 270 220 315 330 300 C470 282 560 195 779 148" fill="none" stroke="#ffffff" stroke-width="2.5"/>
    <g fill="var(--sky)">
      <rect x="6" y="212" width="26" height="15" rx="7" transform="rotate(20 19 219)"/>
      <rect x="44" y="230" width="26" height="15" rx="7" transform="rotate(18 57 237)"/>
      <rect x="84" y="248" width="26" height="15" rx="7" transform="rotate(14 97 255)"/>
      <rect x="124" y="262" width="26" height="15" rx="7" transform="rotate(10 137 269)"/>
      <rect x="165" y="272" width="26" height="15" rx="7" transform="rotate(6 178 279)"/>
      <rect x="206" y="278" width="26" height="15" rx="7" transform="rotate(2 219 285)"/>
      <rect x="248" y="279" width="26" height="15" rx="7" transform="rotate(-2 261 286)"/>
      <rect x="290" y="275" width="26" height="15" rx="7" transform="rotate(-5 303 282)"/>
    </g>
    <rect x="0" y="1105" width="779" height="95" fill="var(--teal)"/>
  </svg>

  <div class="brand">
    <span class="brand-mark"></span><span class="brand-name">BRAMBLE OAK ACADEMY</span>
    <span class="brand-tagline">A Foundation For The Future.</span>
  </div>
  <p class="address">4120 LINDEN COURT<br>LARKFIELD, CO 80455</p>

  <ul class="contact">
    <li class="web"><svg viewBox="0 0 20 20"><circle cx="10" cy="10" r="8" fill="none" stroke="currentColor" stroke-width="1.6"/><rect x="9" y="8.5" width="2" height="6" fill="currentColor"/><circle cx="10" cy="6" r="1.2" fill="currentColor"/></svg>WWW.BRAMBLEOAKACADEMY.NET</li>
    <li class="mail"><svg viewBox="0 0 20 20"><rect x="2" y="4.5" width="16" height="11" fill="none" stroke="currentColor" stroke-width="1.6"/><path d="M2 4.5 L10 11 L18 4.5" fill="none" stroke="currentColor" stroke-width="1.6"/></svg>NORAWHITFIELD@BRAMBLEOAKACADEMY.NET</li>
    <li class="phone"><svg viewBox="0 0 20 20"><path d="M2 8 C2 4 18 4 18 8 L14 9 L13 7 C11 6.5 9 6.5 7 7 L6 9 Z" fill="currentColor"/><rect x="4" y="11" width="12" height="6" rx="1" fill="currentColor"/></svg>720.555.0148</li>
  </ul>

  <div class="hands" role="img" aria-label="Illustration of raised hands painted in bright colours"></div>

  <div class="ribbon">
    <svg width="286" height="62" viewBox="0 0 286 62" aria-hidden="true"><path d="M0 6 L286 0 L270 31 L286 62 L0 62 L16 34 Z" fill="var(--ribbon)"/></svg>
    <span class="ribbon-text">EARLY BIRD SPECIAL</span>
  </div>

  <h2 class="about-title hand">About Us</h2>
  <div class="about">
    <p>Our mission is to provide every child with a quality education and build a foundation for the future.</p>
    <p>We offer preschool to <u>potty-trained</u> children ages 3 years to 4 years old. We are very dedicated and experienced in the developmental stages of these important years.</p>
    <p>With a specialized curriculum, you can be assured that your child will be prepared when entering the world of education</p>
    <p>Mrs. Whitfield is a LICENSED teacher with 10+ years of Elementary School experience. She knows what your child needs to be prepared for the rigor of K-12 education, and how to build that foundation for the future.</p>
  </div>

  <p class="special hand">Enroll before March 31, 2016 and we will waive the application fee! *</p>

  <h2 class="offer-title hand">We Offer</h2>
  <ul class="offer">
    <li><svg viewBox="0 0 20 20"><circle cx="10" cy="10" r="8.5" fill="none" stroke="#fff" stroke-width="1.6"/><path d="M10 4 L11.6 8.2 L16 8.4 L12.6 11.1 L13.8 15.4 L10 13 L6.2 15.4 L7.4 11.1 L4 8.4 L8.4 8.2 Z" fill="#fff"/></svg>Monday through Friday classes. <em>Please call for more information on schedules.</em></li>
    <li><svg viewBox="0 0 20 20"><circle cx="10" cy="10" r="8.5" fill="none" stroke="#fff" stroke-width="1.6"/><path d="M10 4 L11.6 8.2 L16 8.4 L12.6 11.1 L13.8 15.4 L10 13 L6.2 15.4 L7.4 11.1 L4 8.4 L8.4 8.2 Z" fill="#fff"/></svg>Competitive rates with high quality education.</li>
    <li><svg viewBox="0 0 20 20"><circle cx="10" cy="10" r="8.5" fill="none" stroke="#fff" stroke-width="1.6"/><path d="M10 4 L11.6 8.2 L16 8.4 L12.6 11.1 L13.8 15.4 L10 13 L6.2 15.4 L7.4 11.1 L4 8.4 L8.4 8.2 Z" fill="#fff"/></svg>Small classes, allowing for individual attention</li>
    <li><svg viewBox="0 0 20 20"><circle cx="10" cy="10" r="8.5" fill="none" stroke="#fff" stroke-width="1.6"/><path d="M10 4 L11.6 8.2 L16 8.4 L12.6 11.1 L13.8 15.4 L10 13 L6.2 15.4 L7.4 11.1 L4 8.4 L8.4 8.2 Z" fill="#fff"/></svg>Lots of creativity, discovery and learning through play in a safe, fun-filled environment</li>
  </ul>

  <div class="kids" role="img" aria-label="Illustration of a row of cartoon children holding hands"></div>

  <section class="enroll-band">
    <h1 class="enroll-title hand">Now Enrolling for Fall 2016!</h1>
    <p class="enroll-call hand">Don't miss out, contact us today - spaces are limited!</p>
    <p class="enroll-forms hand">All forms available online at www.brambleoakacademy.net</p>
  </section>

  <p class="footnote">* You must be accepted &amp; enrolled for application fee to be waived.</p>
</main>
</body>
</html>
```